Method 17 Product Guide featuring the RV-18 Tarnwell Unit

We need a brochure on the products needed to collect a sample from a smoke stack in accordance with NBR Method 17. The feature item is the RV-18 Tarnwell Unit (metering console) and there are several complementary items associated with the system. We need paragraph to explain each item in the system. See attached draft document. The brochure shall be a minimum of 4 pages , or 8 pages max.

Colors
33a6d7

```html
<!DOCTYPE html>
<html lang="en">
<head>
<meta charset="utf-8">
<title>NBR Method 17 Product Guide – RV-18 Tarnwell Unit</title>
<link href="https://fonts.googleapis.com/css2?family=Open+Sans:wght@400;600;700&display=swap" rel="stylesheet">
<style>
  :root {
    --backdrop: #e2e2e2;
    --page-dark: #3b3a3c;
    --band-black: #141414;
    --panel-gray: #2f2f31;
    --text-light: #e6e6e6;
    --text-muted: #b9b9bb;
    --white: #ffffff;
    --yellow: #f2b705;
    --yellow-light: #f7c82e;
    --blue: #33a6d7;
    --blue-light: #5bbbe4;
  }
  * { box-sizing: border-box; margin: 0; padding: 0; }
  html, body { width: 1150px; height: 1200px; overflow: hidden; }
  body {
    background: var(--backdrop);
    font-family: "Open Sans", sans-serif;
    display: flex;
    flex-direction: column;
    align-items: center;
    justify-content: center;
    gap: 40px;
  }
  .spread {
    width: 800px;
    height: 566px;
    display: flex;
    box-shadow: 0 6px 18px rgba(0,0,0,0.18);
  }
  .spread--yellow { --accent: var(--yellow); --accent-light: var(--yellow-light); }
  .spread--blue { --accent: var(--blue); --accent-light: var(--blue-light); }

  /* Inner item page */
  .spec-page {
    position: relative;
    width: 400px;
    height: 566px;
    background: var(--page-dark);
    color: var(--text-light);
    padding: 26px 30px 0 30px;
  }
  .spec-title {
    font-size: 13px;
    font-weight: 700;
    color: var(--white);
    line-height: 1.2;
  }
  .spec-intro {
    font-size: 7.5px;
    line-height: 1.45;
    color: var(--text-muted);
    margin: 3px 0 9px;
  }
  .spec-block { margin-bottom: 7px; }
  .spec-heading {
    color: var(--accent);
    font-size: 9.5px;
    font-weight: 700;
    margin-bottom: 1px;
  }
  .spec-text {
    font-size: 7.5px;
    line-height: 1.45;
  }
  .diagram-frame {
    position: absolute;
    left: 26px;
    right: 26px;
    bottom: 34px;
    height: 172px;
    border: 6px solid var(--accent);
    background: #f1f1f1;
    border-radius: 3px;
  }
  .diagram-placeholder {
    width: 100%;
    height: 100%;
    background: linear-gradient(135deg, #f4f4f4, #dcdcdc);
  }
  .edge-tab {
    position: absolute;
    left: 0;
    width: 14px;
    height: 46px;
    background: var(--accent);
  }
  .edge-tab--upper { bottom: 150px; }
  .edge-tab--lower { bottom: 50px; }
  .folio {
    position: absolute;
    left: 30px;
    bottom: 12px;
    font-size: 8px;
    font-weight: 600;
    color: var(--text-muted);
  }

  /* Cover page */
  .cover-page { width: 400px; height: 566px; }
  .cover-page svg { display: block; }
  .fill-accent { fill: var(--accent); }
  .fill-accent-light { fill: var(--accent-light); }
  .fill-black { fill: var(--band-black); }
  .fill-gray { fill: var(--panel-gray); }
  .brand-name {
    font-family: "Open Sans", sans-serif;
    font-weight: 700;
    letter-spacing: 1px;
  }
  .brand-name--small { fill: var(--band-black); font-size: 13px; }
  .brand-name--large { fill: var(--white); font-size: 26px; }
  .cover-subtitle {
    font-family: "Open Sans", sans-serif;
    font-weight: 600;
    font-size: 12px;
    fill: var(--white);
  }
  .cover-url {
    font-family: "Open Sans", sans-serif;
    font-size: 11px;
    fill: var(--band-black);
  }
</style>
</head>
<body>

<!-- Spread in yellow: pages 1–2 -->
<section class="spread spread--yellow">
  <article class="spec-page">
    <h2 class="spec-title">RV-18 Tarnwell Unit</h2>
    <p class="spec-intro">The metering console at the heart of the NBR Method 17 sampling system, controlling probe and oven heat, flow and vacuum for in-stack particulate sampling.</p>
    <div class="spec-block">
      <h3 class="spec-heading">Probe and Oven Temperature Control:</h3>
      <p class="spec-text">Kelto PR3 Compact, 1/32 DIN self-tuning PID temperature controller with 3 button keypad. SSR Driver for 25 amp solid state relay. Type K thermocouple jack for input.</p>
    </div>
    <div class="spec-block">
      <h3 class="spec-heading">Pressure Transducers:</h3>
      <p class="spec-text">High Resolution Digital sensor. Factory calibrated and temperature compensated -20C to 70C. Proof pressure 48 kPa. Accuracy better than 0.25%. ΔP +/- 5.0" H₂O Range Bi-Directional with 0.001" Resolution.</p>
    </div>
    <div class="spec-block">
      <h3 class="spec-heading">Vacuum Gauge:</h3>
      <p class="spec-text">Bourdon tube, Dual Scale, 0 to -30" Hg, 0 to -100 kPa. Umbilical Connection: multi-conductor circular connector. Sample Inlet: 1/2". Pitot Connections: 1/4". Type K Inputs: Aux, Stack, Probe, Oven, Exit.</p>
    </div>
    <div class="spec-block">
      <h3 class="spec-heading">Power:</h3>
      <p class="spec-text">Supply 120VAC/60 Hz 15 amps max. or 240VAC/50 Hz 10 amps max. IEC C-13 Inlet.</p>
    </div>
    <div class="spec-block">
      <h3 class="spec-heading">Dimensions:</h3>
      <p class="spec-text">H17" x W17" x D12" (43 cm x 43 cm x 30.5 cm). Weight: 40 lbs (18 kg).</p>
    </div>
    <span class="edge-tab edge-tab--upper"></span>
    <span class="edge-tab edge-tab--lower"></span>
    <div class="diagram-frame">
      <div class="diagram-placeholder" role="img" aria-label="Diagram of the RV-18 Tarnwell Unit Method 17 sampling train with probe, umbilical cables and metering console"></div>
    </div>
    <span class="folio">Page 2 of 4</span>
  </article>

  <article class="cover-page">
    <svg width="400" height="566" viewBox="0 0 400 566">
      <defs>
        <linearGradient id="plant-photo-y" x1="0" y1="0" x2="0" y2="1">
          <stop offset="0" stop-color="#6f95c2"/>
          <stop offset="0.35" stop-color="#c9d6e4"/>
          <stop offset="0.6" stop-color="#a89f8c"/>
          <stop offset="1" stop-color="#6d6455"/>
        </linearGradient>
      </defs>
      <rect width="400" height="566" fill="url(#plant-photo-y)" role="img" aria-label="Photograph of an industrial plant with two smoke stacks under a cloudy blue sky"/>
      <polygon class="fill-gray" points="400,0 400,205 120,115"/>
      <polygon class="fill-black" points="0,140 400,0 400,30 0,190"/>
      <polygon class="fill-accent" points="0,0 400,0 0,140"/>
      <polygon class="fill-accent-light" points="0,60 300,0 400,0 0,105"/>
      <text class="brand-name brand-name--small" x="24" y="62">CORVANE INSTRUMENTS</text>
      <text class="brand-name brand-name--large" x="60" y="290">CORVANE</text>
      <text class="brand-name brand-name--large" x="60" y="322">INSTRUMENTS</text>
      <text class="cover-subtitle" x="60" y="346">NBR Method 17 Product Guide</text>
      <text class="cover-subtitle" x="60" y="362">Featuring the RV-18 Tarnwell Unit</text>
      <polygon class="fill-gray" points="0,400 0,566 250,566"/>
      <polygon class="fill-black" points="90,566 400,420 400,460 170,566"/>
      <polygon class="fill-accent" points="170,566 400,460 400,566"/>
      <polygon class="fill-accent-light" points="230,566 400,486 400,510 285,566"/>
      <text class="cover-url" x="282" y="552">www.corvaneinst.com</text>
    </svg>
  </article>
</section>

<!-- Spread in blue: pages 3–4 -->
<section class="spread spread--blue">
  <article class="spec-page">
    <h2 class="spec-title">Method 17 System Items</h2>
    <p class="spec-intro">Complementary items that connect to the RV-18 Tarnwell Unit to complete the NBR Method 17 stack sampling train.</p>
    <div class="spec-block">
      <h3 class="spec-heading">Sample Probe:</h3>
      <p class="spec-text">Heated stainless steel probe with in-stack filter holder and Type S pitot tube. Places the filter inside the stack so particulate is caught at stack temperature.</p>
    </div>
    <div class="spec-block">
      <h3 class="spec-heading">Umbilical Cable:</h3>
      <p class="spec-text">Combined sample line, pitot lines and thermocouple leads in one jacket. Quick connects join the probe to the console in seconds.</p>
    </div>
    <div class="spec-block">
      <h3 class="spec-heading">Impinger Case:</h3>
      <p class="spec-text">Ice-bath case holding the glass impingers that cool the gas and collect moisture before it reaches the metering console.</p>
    </div>
    <div class="spec-block">
      <h3 class="spec-heading">Thermocouple Leads:</h3>
      <p class="spec-text">Type K leads for stack, probe, oven and exit points, read live on the console display.</p>
    </div>
    <div class="spec-block">
      <h3 class="spec-heading">Calibration Kit:</h3>
      <p class="spec-text">Orifice set and fittings for leak checks and meter calibration before each test run.</p>
    </div>
    <span class="edge-tab edge-tab--upper"></span>
    <span class="edge-tab edge-tab--lower"></span>
    <div class="diagram-frame">
      <div class="diagram-placeholder" role="img" aria-label="Diagram of the complete Method 17 sampling train joined to the RV-18 Tarnwell Unit"></div>
    </div>
    <span class="folio">Page 4 of 4</span>
  </article>

  <article class="cover-page">
    <svg width="400" height="566" viewBox="0 0 400 566">
      <defs>
        <linearGradient id="plant-photo-b" x1="0" y1="0" x2="0" y2="1">
          <stop offset="0" stop-color="#6f95c2"/>
          <stop offset="0.35" stop-color="#c9d6e4"/>
          <stop offset="0.6" stop-color="#a89f8c"/>
          <stop offset="1" stop-color="#6d6455"/>
        </linearGradient>
      </defs>
      <rect width="400" height="566" fill="url(#plant-photo-b)" role="img" aria-label="Photograph of an industrial plant with two smoke stacks under a cloudy blue sky"/>
      <polygon class="fill-gray" points="400,0 400,205 120,115"/>
      <polygon class="fill-black" points="0,140 400,0 400,30 0,190"/>
      <polygon class="fill-accent" points="0,0 400,0 0,140"/>
      <polygon class="fill-accent-light" points="0,60 300,0 400,0 0,105"/>
      <text class="brand-name brand-name--small" x="24" y="62">CORVANE INSTRUMENTS</text>
      <text class="brand-name brand-name--large" x="60" y="290">CORVANE</text>
      <text class="brand-name brand-name--large" x="60" y="322">INSTRUMENTS</text>
      <text class="cover-subtitle" x="60" y="346">NBR Method 17 Product Guide</text>
      <text class="cover-subtitle" x="60" y="362">Featuring the RV-18 Tarnwell Unit</text>
      <polygon class="fill-gray" points="0,400 0,566 250,566"/>
      <polygon class="fill-black" points="90,566 400,420 400,460 170,566"/>
      <polygon class="fill-accent" points="170,566 400,460 400,566"/>
      <polygon class="fill-accent-light" points="230,566 400,486 400,510 285,566"/>
      <text class="cover-url" x="282" y="552">www.corvaneinst.com</text>
    </svg>
  </article>
</section>

</body>
</html>
```